Etiketten-Design für Produkte eines Familienbetriebs mit Imkerei und Hühnerhaltung
Zielgruppe
Wir sind ein Familienbetrieb mit Imkerei und Hühnerhaltung. Wir suchen für unsere Produkte ein modernes Corporate Design, mit zentralen, bei jedem Produkt vorkommenden Elementen, sowie Elementen, welche produktindividuell sind.
Wir leben in einem 150 jährigen Riegelhaus, welches in der Umgebung sehr bekannt ist. Es soll im Etiketten-Design zentral erscheinen.
Unsere Produkte sind: Honig, Pollen, Eier
Aufgabenstellung
1. Zentrale, auf allen Etiketten wiederkehrende Elemente:
- Unser Riegelhaus (stilisiert) (Bild beiliegend)
- Das Wort 'Birkacher' (Anmerkung: ohne Anführungszeichen)
- die zentralen Elemente sollen die Produkte nicht überragen.
2. Dezente Adresse:
- Familie Dorlitz, Birkenau, CH-8763 Lindwil
3. Produkte:
a) Honig
Sorten: Waldhonig (dunkel), Blütenhonig (gelblich-goldig), Crèmehonig (gelblich-weisslich), Lavendelhonig (gelblich-goldig)
Die Honigsorten sollen farblich hervortreten.
Freifeld (zweizeilig): für die Lotnummer und die Haltbarkeitsangabe)
Gewicht: 250 g, 500 g
b) Pollen
Gewicht: 100 g
c) Eier
Verpackungseinheiten: 4er-, 6er-, 10er-Packung
Haltungsform: BIO-Haltung
das Wort 'frisch'
Farbe grün (=Bio) soll farblich hervortreten (ähnlich wie beim Honig)
Freifeld (zweizeilig: für das Eigewicht und die Haltbarkeitsangabe)
Bitte keine Stock-Bilder verwenden. Die Etiketten sollen schlicht, edel ,schörkellos und modern erscheinen.
Das Etikett soll Exklusivität und Qualität ausstrahlen. Etikettenhintergrund einfarbig.
Interessanterweise gibt es bei Weinen solche Etiketten. Ich habe einige rausgesucht und angehängt, um die Richtung vorzugeben. (Wein1-6)
Ich habe auch eine schlichte Honigetikette gefunden, die ins Schema passt. (Imker1)
Zusätzlich sind jetzt auch noch Farbbeispiele der Honigsorten zur besseren Abstimmung von Inhalt und Etikette beigelegt. Lavendelhonig ist dem Blütenhonig sehr ähnlich.
Etikettengrössen:
Honig/Pollen 250 g: 190 x 42 mm
Honig 500 g: 206 x 45 mm
Eier 4er: 60 x 60 mm
Eier 6er: 110 x 60 mm
Eier 10er: 170 x 60 cm

```html
<!DOCTYPE html>
<html lang="de">
<head>
<meta charset="utf-8">
<title>Birkacher – Etiketten</title>
<link href="https://fonts.googleapis.com/css2?family=Alegreya:wght@500&family=Arimo:wght@400;700&family=Roboto+Condensed:wght@700&family=Source+Sans+3:wght@400&display=swap" rel="stylesheet">
<style>
  :root{
    --paper:#ffffff;
    --cream:#fdf7cf;
    --cream-soft:#fcf8d2;
    --brown:#7b4a1f;
    --green:#4f9a66;
    --gold:#d3ae2e;
    --lavender:#8878a0;
    --seal:#7ab648;
  }
  *{margin:0;padding:0;box-sizing:border-box}
  html,body{width:1065px;height:1200px;overflow:hidden;background:var(--paper)}
  .board{position:relative;width:1065px;height:1200px}

  .comb-field{position:absolute;top:0;height:210px;width:367px}
  .comb-field--left{left:0;background:linear-gradient(135deg,rgba(226,194,90,.22),rgba(226,194,90,0) 85%)}
  .comb-field--right{right:0;background:linear-gradient(225deg,rgba(226,194,90,.22),rgba(226,194,90,0) 85%)}

  .brand-disc{position:absolute;left:441px;top:41px;width:184px;height:184px;border-radius:50%;background:var(--cream-soft);
    display:flex;flex-direction:column;align-items:center;justify-content:center;padding-top:60px}
  .wordmark{font-family:"Alegreya",serif;font-weight:500;color:var(--brown);line-height:1}
  .brand-disc .wordmark{font-size:32px}
  .tagline{font-family:"Source Sans 3",sans-serif;letter-spacing:.14em;text-transform:uppercase;color:var(--brown)}
  .brand-disc .tagline{font-size:7.5px;margin-top:4px}

  .intro{position:absolute;left:201px;top:256px;width:660px;font-family:"Source Sans 3",sans-serif;font-size:16.6px;line-height:20.5px;color:var(--brown)}

  .label{position:absolute;width:420px;height:93px;background:var(--cream);box-shadow:0 2px 5px rgba(0,0,0,.25);color:var(--c)}
  .label--creme{left:97px;top:351px;--c:var(--brown)}
  .label--wald{left:558px;top:351px;--c:var(--green)}
  .label--bluete{left:97px;top:467px;--c:var(--gold)}
  .label--lavendel{left:558px;top:467px;--c:var(--lavender)}
  .label__band{position:absolute;left:0;top:0;width:111px;height:93px;background:var(--c)}
  .label__comb{position:absolute;left:53px;top:0;width:100px;height:38px;background:linear-gradient(90deg,rgba(255,255,255,.18),rgba(0,0,0,.06) 55%,rgba(0,0,0,0))}
  .label__variety{position:absolute;left:0;width:111px;top:61px;text-align:center;font-family:"Arimo",sans-serif;font-weight:700;font-size:11px;color:#fff}
  .label__kind{position:absolute;left:0;width:111px;top:76px;text-align:center;font-family:"Arimo",sans-serif;font-size:4.6px;letter-spacing:.12em;color:rgba(255,255,255,.9)}
  .label__brand{position:absolute;left:118px;width:160px;top:50px;text-align:center}
  .label__brand .wordmark{font-size:26px;color:var(--c)}
  .label__brand .tagline{font-size:6.3px;color:var(--c);margin-top:1px}
  .label__bio{position:absolute;right:14px;top:7px;font-family:"Roboto Condensed",sans-serif;font-weight:700;font-size:9.5px}
  .label__seal{position:absolute;right:14px;top:19px;width:51px;height:18px;border-radius:2px;background:var(--seal)}
  .label__net{position:absolute;right:17px;top:57px;font-family:"Roboto Condensed",sans-serif;font-weight:700;font-size:9px}
  .label__net small{font-family:"Arimo",sans-serif;font-weight:400;font-size:4.5px;letter-spacing:.08em;margin-right:3px}
  .label__origin,.label__address{position:absolute;right:17px;font-family:"Arimo",sans-serif;font-size:4.5px;letter-spacing:.1em}
  .label__origin{top:73px}
  .label__address{top:81px;letter-spacing:.06em}

  .jar-seal{position:absolute;left:265px;top:645px;width:58px;height:175px;background:var(--brown)}
  .jar-label{position:absolute;left:100px;top:798px;width:387px;height:188px;background:var(--cream)}
  .jar-label__band{position:absolute;left:0;top:0;width:19px;height:100%;background:var(--brown)}
  .jar-label__comb{position:absolute;left:19px;top:0;width:52px;height:80px;background:linear-gradient(180deg,rgba(123,74,31,.08),rgba(123,74,31,0))}
  .jar-label__brand{position:absolute;left:60px;width:300px;top:104px;text-align:center}
  .jar-label__brand .wordmark{font-size:54px}
  .jar-label__brand .tagline{font-size:12px;margin-top:4px}

  .lid{position:absolute;left:465px;top:805px;width:316px;height:316px;border-radius:50%;overflow:hidden;background:var(--cream)}
  .lid__brand{position:absolute;left:0;width:100%;top:70px;text-align:center}
  .lid__brand .wordmark{font-size:19px}
  .lid__brand .tagline{font-size:4.5px;margin-top:2px}
  .lid__band{position:absolute;left:0;top:131px;width:100%;height:185px;background:var(--brown);color:var(--cream);text-align:center}
  .lid__variety{font-family:"Arimo",sans-serif;font-weight:700;font-size:24px;margin-top:24px}
  .lid__dots{width:180px;margin:6px auto 0;border-top:3px dotted var(--cream)}
  .lid__kind{font-family:"Arimo",sans-serif;font-size:8.5px;letter-spacing:.16em;margin-top:9px}
  .lid__weight{font-family:"Roboto Condensed",sans-serif;font-weight:700;font-size:22px;margin-top:42px;display:flex;align-items:center;justify-content:center;gap:12px}
  .lid__weight::before,.lid__weight::after{content:"";width:24px;border-top:1.5px solid var(--cream)}
</style>
</head>
<body>
<main class="board">
  <div class="comb-field comb-field--left" role="img" aria-label="Wabenmuster"></div>
  <div class="comb-field comb-field--right" role="img" aria-label="Wabenmuster"></div>

  <div class="brand-disc">
    <span class="wordmark">Birkacher</span>
    <span class="tagline">Family Dorlitz</span>
  </div>

  <p class="intro">Label design is made of soft colors, the house is stylized and harmoniously fits into the style of the label design. It is associated with home warmth and coziness, delicious food and the smell of the farm.</p>

  <section class="label label--creme">
    <div class="label__band"></div>
    <div class="label__comb" role="img" aria-label="Wabenmuster"></div>
    <div class="label__variety">Crèmehonig</div>
    <div class="label__kind">NATÜRLICHE HONIGPRODUKTE</div>
    <div class="label__brand"><div class="wordmark">Birkacher</div><div class="tagline">Family Dorlitz</div></div>
    <div class="label__bio">BIO-IMKEREI</div>
    <div class="label__seal"></div>
    <div class="label__net"><small>Netto</small>250 g</div>
    <div class="label__origin">HONIG AUS DEM SCHWEIZ</div>
    <div class="label__address">Familie Dorlitz, Birkenau, CH-8763 Lindwil</div>
  </section>

  <section class="label label--wald">
    <div class="label__band"></div>
    <div class="label__comb" role="img" aria-label="Wabenmuster"></div>
    <div class="label__variety">Waldhonig</div>
    <div class="label__kind">NATÜRLICHE HONIGPRODUKTE</div>
    <div class="label__brand"><div class="wordmark">Birkacher</div><div class="tagline">Family Dorlitz</div></div>
    <div class="label__bio">BIO-IMKEREI</div>
    <div class="label__seal"></div>
    <div class="label__net"><small>Netto</small>250 g</div>
    <div class="label__origin">HONIG AUS DEM SCHWEIZ</div>
    <div class="label__address">Familie Dorlitz, Birkenau, CH-8763 Lindwil</div>
  </section>

  <section class="label label--bluete">
    <div class="label__band"></div>
    <div class="label__comb" role="img" aria-label="Wabenmuster"></div>
    <div class="label__variety">Blütenhonig</div>
    <div class="label__kind">NATÜRLICHE HONIGPRODUKTE</div>
    <div class="label__brand"><div class="wordmark">Birkacher</div><div class="tagline">Family Dorlitz</div></div>
    <div class="label__bio">BIO-IMKEREI</div>
    <div class="label__seal"></div>
    <div class="label__net"><small>Netto</small>250 g</div>
    <div class="label__origin">HONIG AUS DEM SCHWEIZ</div>
    <div class="label__address">Familie Dorlitz, Birkenau, CH-8763 Lindwil</div>
  </section>

  <section class="label label--lavendel">
    <div class="label__band"></div>
    <div class="label__comb" role="img" aria-label="Wabenmuster"></div>
    <div class="label__variety">Lavendelhonig</div>
    <div class="label__kind">NATÜRLICHE HONIGPRODUKTE</div>
    <div class="label__brand"><div class="wordmark">Birkacher</div><div class="tagline">Family Dorlitz</div></div>
    <div class="label__bio">BIO-IMKEREI</div>
    <div class="label__seal"></div>
    <div class="label__net"><small>Netto</small>250 g</div>
    <div class="label__origin">HONIG AUS DEM SCHWEIZ</div>
    <div class="label__address">Familie Dorlitz, Birkenau, CH-8763 Lindwil</div>
  </section>

  <div class="jar-seal"></div>
  <section class="jar-label">
    <div class="jar-label__band"></div>
    <div class="jar-label__comb" role="img" aria-label="Wabenmuster"></div>
    <div class="jar-label__brand"><div class="wordmark">Birkacher</div><div class="tagline">Family Dorlitz</div></div>
  </section>

  <section class="lid">
    <div class="lid__brand"><div class="wordmark">Birkacher</div><div class="tagline">Family Dorlitz</div></div>
    <div class="lid__band">
      <div class="lid__variety">Crèmehonig</div>
      <div class="lid__dots"></div>
      <div class="lid__kind">NATÜRLICHE HONIGPRODUKTE</div>
      <div class="lid__weight">250 g</div>
    </div>
  </section>
</main>
</body>
</html>
```